Lanternleaf - Fresh Asian Cuisine Menu

We need to redo our menu to include pictures of food items. Our restaurant is vibrant, trendy, upscale Chinese cuisine

Requirements
Must have
• Must fit on 8.5x11 paper. We can remove the About Us section if needed but menu cannot be more than 6 pages total. Must include pictures of menu items

```html
<!DOCTYPE html>
<html lang="en">
<head>
<meta charset="utf-8">
<title>Lanternleaf - Fresh Asian Cuisine Menu</title>
<link href="https://fonts.googleapis.com/css2?family=Source+Serif+4:wght@400;700&family=Oswald:wght@600&display=swap" rel="stylesheet">
<style>
  :root {
    --backdrop: #e6e6e6;
    --paper: #ffffff;
    --ink: #1a1a1a;
    --ink-soft: #3a3a3a;
    --chili: #d42a1c;
    --rule: #8a8a8a;
    --banner-dark: #2a2226;
    --banner-mid: #5a3a3e;
    --footer-line: #6a1a0c;
  }
  * { box-sizing: border-box; margin: 0; padding: 0; }
  html, body { width: 1200px; height: 848px; overflow: hidden; }
  body {
    background: var(--backdrop);
    font-family: "Source Serif 4", Georgia, serif;
    color: var(--ink);
    position: relative;
  }
  .menu-page {
    position: absolute;
    left: 327px; top: 51px;
    width: 550px; height: 711px;
    background: var(--paper);
    box-shadow: 0 2px 8px rgba(0,0,0,.25);
    overflow: hidden;
  }
  .top-strip {
    position: absolute; left: 0; top: 0; width: 100%; height: 17px;
    background: linear-gradient(90deg, #3c5a2a 0%, #2a2a30 20%, #4a4a52 50%, #2a2a30 80%, #3a3a40 100%);
  }
  .masthead {
    position: absolute; left: 0; top: 17px; width: 100%; height: 108px;
    display: flex; flex-direction: column; align-items: center; justify-content: center;
  }
  .brand-name {
    font-weight: 700; font-size: 46px; line-height: 1; color: var(--ink);
  }
  .brand-tagline {
    margin-top: 6px;
    font-weight: 700; font-size: 13px; letter-spacing: 2px; color: var(--ink);
  }
  .banner-photo {
    position: absolute; left: 3px; top: 125px; width: 544px; height: 260px;
    background: linear-gradient(to bottom, var(--banner-dark) 0%, var(--banner-mid) 18%, #6b6066 45%, #b8b4b6 75%, #ffffff 100%);
  }
  .section-title {
    position: absolute; left: 0; top: 130px; width: 100%;
    text-align: center;
    font-family: "Oswald", "Arial Narrow", sans-serif;
    font-weight: 600; font-size: 23px; line-height: 32px; color: #fff; letter-spacing: .5px;
  }
  .menu-card {
    position: absolute; left: 21px; top: 166px; width: 511px; height: 415px;
    background: var(--paper);
    padding: 14px 12px 0 13px;
    display: flex; gap: 14px;
  }
  .menu-column { width: 236px; }
  .menu-item {
    padding-bottom: 6px; margin-bottom: 10px;
    border-bottom: 1px dotted var(--rule);
  }
  .menu-item.last { border-bottom: none; }
  .item-head { display: flex; justify-content: space-between; align-items: baseline; height: 13px; }
  .item-name { font-weight: 700; font-size: 10.3px; display: flex; align-items: center; gap: 2px; }
  .item-price { font-size: 9px; }
  .item-desc { font-size: 8.1px; line-height: 11px; color: var(--ink-soft); max-width: 206px; }
  .item-note { font-weight: 700; font-size: 7.8px; margin-top: 8px; }
  .chili { width: 11px; height: 8px; }
  .photo-grid {
    position: absolute; left: 79px; top: 587px;
    display: grid; grid-template-columns: repeat(6, 58px); column-gap: 9px; row-gap: 11px;
  }
  .dish-photo { width: 58px; height: 38px; }
  .footer-rule {
    position: absolute; left: 21px; top: 689px; width: 511px; height: 5px;
    background: linear-gradient(to bottom, #2a0a04, var(--footer-line));
  }
</style>
</head>
<body>
<svg width="0" height="0" style="position:absolute">
  <defs>
    <symbol id="chili" viewBox="0 0 12 8">
      <path d="M1 6.5 C4 7.5 9 5 10.5 1.5 L11.5 2 C10.5 6 5 8.5 1 6.5Z" fill="#d42a1c"/>
      <path d="M10.3 1.6 L11.2 0.3" stroke="#3a7a2a" stroke-width="1"/>
    </symbol>
  </defs>
</svg>

<main class="menu-page">
  <div class="top-strip" role="img" aria-label="Dark strip of a restaurant table photo"></div>

  <header class="masthead">
    <div class="brand-name">Lanternleaf</div>
    <div class="brand-tagline">FRESH ASIAN CUISINE</div>
  </header>

  <div class="banner-photo" role="img" aria-label="Photo of a stir-fried dish with vegetables and noodles"></div>
  <h1 class="section-title">APPETIZERS</h1>

  <section class="menu-card">
    <div class="menu-column">
      <div class="menu-item"><div class="item-head"><span class="item-name">Edamame</span><span class="item-price">$4</span></div><p class="item-desc">Seasoned &amp; boiled soy bean</p></div>
      <div class="menu-item"><div class="item-head"><span class="item-name">Scallion Pancakes</span><span class="item-price">$6</span></div><p class="item-desc">Traditional Chinese flatbread folded with oil and minced scallions and pan fried</p></div>
      <div class="menu-item"><div class="item-head"><span class="item-name">Lanternleaf Lettuce Wraps</span><span class="item-price">$8</span></div><p class="item-desc">Seasoned ground chicken drizzled with our top secret homemade sauce served with lettuce wraps</p></div>
      <div class="menu-item"><div class="item-head"><span class="item-name">Salt &amp; Pepper Calamari</span><span class="item-price">$9</span></div><p class="item-desc">Crispy Calamari with Green &amp; red peppers and onions</p></div>
      <div class="menu-item"><div class="item-head"><span class="item-name">Buddha Bang Shrimp</span><span class="item-price">$9</span></div><p class="item-desc">Crispy fried shrimp tossed in our creamy spicy sauce</p></div>
      <div class="menu-item"><div class="item-head"><span class="item-name">Drunken Chicken <svg class="chili"><use href="#chili"/></svg></span><span class="item-price">$8</span></div><p class="item-desc">Chicken, Thai chili in a house made spicy sauce</p></div>
      <div class="menu-item"><div class="item-head"><span class="item-name">Sichuan Spiced Beef <svg class="chili"><use href="#chili"/></svg><svg class="chili"><use href="#chili"/></svg></span><span class="item-price">$9</span></div><p class="item-desc">Beef Shank, beef tripe, cilantro, peanuts and celery</p></div>
      <div class="menu-item last"><div class="item-head"><span class="item-name">Beef Crispy Bottom Bao</span><span class="item-price">$10</span></div><p class="item-desc">Pan fried crispy bottom Bao, stuffed with beef, drizzled with scallion and sesame (Fresh made to order, takes at least 20 mins to serve)</p><p class="item-note">add Shrimp $1</p></div>
    </div>
    <div class="menu-column">
      <div class="menu-item"><div class="item-head"><span class="item-name">Crispy Mala Beef Jerky <svg class="chili"><use href="#chili"/></svg><svg class="chili"><use href="#chili"/></svg></span><span class="item-price">$9</span></div><p class="item-desc">Dry fried shredded beef with various peppers in sesame and peppercorn oil</p></div>
      <div class="menu-item"><div class="item-head"><span class="item-name">Fried Chicken Dumplings (6)</span><span class="item-price">$6</span></div><p class="item-desc">Chinese dumpling stuffed with Chicken, Shiitake mushrooms and bamboo shoots</p></div>
      <div class="menu-item"><div class="item-head"><span class="item-name">Red Oil Dumplings (6) <svg class="chili"><use href="#chili"/></svg></span><span class="item-price">$7</span></div><p class="item-desc">Chicken filled dumplings in Sichuan red oil sauce drizzled with sesame</p></div>
      <div class="menu-item"><div class="item-head"><span class="item-name">Pork Egg Rolls (2)</span><span class="item-price">$4</span></div><p class="item-desc">Hand rolled with julienned veggies with our sweet n' sour mustard sauce</p></div>
      <div class="menu-item"><div class="item-head"><span class="item-name">Vegetarian Spring Rolls (3)</span><span class="item-price">$4</span></div><p class="item-desc">Traditional Asian Roll served with a sweet chili sauce</p></div>
      <div class="menu-item"><div class="item-head"><span class="item-name">Garlic Cucumber Salad</span><span class="item-price">$7</span></div><p class="item-desc">Sliced cucumber with a garlic vinaigrette</p></div>
      <div class="menu-item"><div class="item-head"><span class="item-name">Hot n' Sour Soup <svg class="chili"><use href="#chili"/></svg></span><span class="item-price">$4</span></div><p class="item-desc">Tangy broth with Bamboo shoot, wood ear mushrooms, tofu, egg and carrots</p></div>
      <div class="menu-item last"><div class="item-head"><span class="item-name">West Lake Soup</span><span class="item-price">$4</span></div><p class="item-desc">Light creamy soup with ground beef, diced Shiitake mushroom, tofu, bamboo shoots, egg white and cilantro</p></div>
    </div>
  </section>

  <div class="photo-grid">
    <div class="dish-photo" role="img" aria-label="Photo of steamed buns" style="background:linear-gradient(135deg,#6a7a6a,#d8d0b8)"></div>
    <div class="dish-photo" role="img" aria-label="Photo of lettuce wraps" style="background:linear-gradient(135deg,#b8a890,#8a6a3a)"></div>
    <div class="dish-photo" role="img" aria-label="Photo of spiced beef" style="background:linear-gradient(135deg,#d8d4cc,#a84a2a)"></div>
    <div class="dish-photo" role="img" aria-label="Photo of calamari" style="background:linear-gradient(135deg,#4a4a5a,#c8a870)"></div>
    <div class="dish-photo" role="img" aria-label="Photo of red oil dumplings" style="background:linear-gradient(135deg,#c82a1a,#e8b080)"></div>
    <div class="dish-photo" role="img" aria-label="Photo of mala beef jerky" style="background:linear-gradient(135deg,#3a3a3a,#8a3a1a)"></div>
    <div class="dish-photo" role="img" aria-label="Photo of drunken chicken" style="background:linear-gradient(135deg,#d87a4a,#3a2a2a)"></div>
    <div class="dish-photo" role="img" aria-label="Photo of fried dumplings" style="background:linear-gradient(135deg,#d8d8d8,#c89a4a)"></div>
    <div class="dish-photo" role="img" aria-label="Photo of spring rolls" style="background:linear-gradient(135deg,#2a2a2a,#c8a060)"></div>
    <div class="dish-photo" role="img" aria-label="Photo of hot and sour soup" style="background:linear-gradient(135deg,#a86a4a,#c8702a)"></div>
    <div class="dish-photo" role="img" aria-label="Photo of west lake soup" style="background:linear-gradient(135deg,#d8d4cc,#8a8a7a)"></div>
    <div class="dish-photo" role="img" aria-label="Photo of cucumber salad" style="background:linear-gradient(135deg,#5a5a5a,#d8c8a0)"></div>
  </div>

  <div class="footer-rule"></div>
</main>
</body>
</html>
```